Need a website where people can find information about the newly formed Northmere Property Review Board. Soon after, we will need a place to publish our findings as we audit each municipality in the State of Wisconsin. I have a logo (designed by Pixel Harbor), a MS Word document showing the content and a set of images to choose from that we can purchase from Snapvine.com (found here https://www.snapvinephoto.example/teamwork/lists/-Qb7TrWmXa2NoPLzdRy-Hk)

```html
<!DOCTYPE html>
<html lang="en">
<head>
<meta charset="UTF-8">
<title>Northmere Property Review Board – Uniform Taxation</title>
<link rel="stylesheet" href="https://fonts.googleapis.com/css2?family=Roboto:wght@400;500;700&family=Work+Sans:wght@800&display=swap">
<style>
  :root {
    --green: #3f8a12;
    --green-dark: #2f6e0a;
    --ink: #111111;
    --body: #555555;
    --white: #ffffff;
    --photo-top: #6f8a5a;
    --photo-bottom: #8a8f74;
  }
  * { box-sizing: border-box; margin: 0; padding: 0; }
  html, body { width: 950px; height: 1200px; overflow: hidden; background: var(--white); }
  body { position: relative; font-family: "Roboto", Arial, sans-serif; color: var(--body); }

  .hero { position: absolute; left: 0; top: 0; width: 950px; height: 400px; }
  .hero-art { position: absolute; left: 0; top: 0; }

  .brand {
    position: absolute; left: 88px; top: 30px;
    display: flex; align-items: center; gap: 8px;
    font-family: "Roboto", Arial, sans-serif; font-weight: 700; font-size: 20px;
    color: var(--white); letter-spacing: .5px;
  }
  .brand-dot { width: 14px; height: 14px; border-radius: 50%; background: var(--green); }

  .main-nav {
    position: absolute; right: 88px; top: 43px;
    display: flex; gap: 24px;
  }
  .main-nav a {
    color: var(--white); text-decoration: none;
    font-weight: 700; font-size: 12px; text-transform: uppercase;
  }

  .scroll-ring {
    position: absolute; left: 429px; top: 312px; width: 92px; height: 92px;
    border-radius: 50%; border: 1px solid var(--white);
    clip-path: inset(0 0 50% 0);
  }
  .scroll-cue {
    position: absolute; left: 449px; top: 332px; width: 52px; height: 52px;
    border-radius: 50%; background: var(--white);
    box-shadow: 0 2px 6px rgba(0,0,0,.2);
    display: flex; align-items: center; justify-content: center;
  }
  .scroll-cue svg { display: block; }

  .intro { position: absolute; left: 87px; top: 430px; width: 776px; text-align: center; }
  .intro h1 {
    font-family: "Work Sans", Arial, sans-serif; font-weight: 800; font-size: 24px;
    color: var(--ink); letter-spacing: .5px; margin-bottom: 28px;
  }
  .intro p { font-size: 12.2px; line-height: 20.4px; margin-bottom: 14px; }

  .causes {
    position: absolute; left: 119px; top: 711px; width: 712px; height: 214px;
    background: var(--white); border-radius: 8px;
    box-shadow: 0 2px 14px rgba(0,0,0,.09);
  }
  .causes ul { position: absolute; top: 30px; list-style: none; }
  .causes ul.col-a { left: 47px; }
  .causes ul.col-b { left: 345px; }
  .causes li {
    display: flex; align-items: center; gap: 12px;
    height: 25.7px; font-size: 11.6px; color: var(--body);
  }
  .causes li svg { flex: none; display: block; }

  .site-footer { position: absolute; left: 0; top: 980px; width: 950px; height: 220px; }
  .footer-band { position: absolute; left: 0; top: 0; }
  .footer-brand {
    position: absolute; left: 0; width: 950px; top: 75px;
    display: flex; justify-content: center; align-items: center; gap: 8px;
    font-weight: 700; font-size: 24px; color: var(--white); letter-spacing: 1px;
  }
  .footer-brand .brand-dot { width: 16px; height: 16px; }
  .footer-rule { position: absolute; left: 88px; width: 774px; top: 172px; height: 1px; background: #444; }
  .copyright { position: absolute; left: 387px; top: 184px; font-size: 11px; color: var(--white); }
  .legal { position: absolute; right: 88px; top: 184px; font-size: 11px; color: var(--white); display: flex; gap: 10px; }
  .legal a { color: var(--white); text-decoration: none; }
</style>
</head>
<body>

<header class="hero">
  <svg class="hero-art" width="950" height="400" viewBox="0 0 950 400">
    <defs>
      <linearGradient id="photoTone" x1="0" y1="0" x2="0" y2="1">
        <stop offset="0" stop-color="var(--photo-top)"/>
        <stop offset="1" stop-color="var(--photo-bottom)"/>
      </linearGradient>
    </defs>
    <path d="M0 0 H950 V246 Q475 475 0 246 Z" fill="var(--green)"/>
    <path d="M0 0 H950 V246 Q475 440 0 246 Z" fill="url(#photoTone)" role="img" aria-label="Aerial photo of a leafy suburban neighbourhood with rows of houses and trees"/>
  </svg>

  <div class="brand"><span class="brand-dot"></span>NPRB</div>

  <nav class="main-nav">
    <a href="#">Home</a>
    <a href="#">Audit Results</a>
    <a href="#">Recommendations</a>
    <a href="#">Blog</a>
    <a href="#">Contact Us</a>
  </nav>

  <div class="scroll-ring"></div>
  <div class="scroll-cue">
    <svg width="18" height="18" viewBox="0 0 18 18"><path d="M9 2 V14 M3.5 9 L9 14.5 L14.5 9" stroke="var(--green)" stroke-width="3" fill="none" stroke-linecap="round" stroke-linejoin="round"/></svg>
  </div>
</header>

<section class="intro">
  <h1>WHAT IS UNIFORM TAXATION?</h1>
  <p>Uniform taxation means similar properties have similar values for taxation purposes.</p>
  <p>For example, if you own a condominium assessed for tax purposes at $200,000 and your neighbor has the same unit but is assessed at $160,000, your values, and therefore your taxes, will be significantly different. You will be paying more of the tax burden than your neighbor, even though the market value of both units is the same. This is non-uniform taxation.</p>
  <p>Two properties are often not identical; but to the extent that they are the same their assessed values should be the same. To the extent they are different their assessed values should be different.</p>
  <p>There are many things that cause non-uniformity when it comes to property taxation. These things include:</p>
</section>

<section class="causes">
  <ul class="col-a">
    <li><svg width="10" height="10" viewBox="0 0 10 10"><circle cx="5" cy="5" r="5" fill="var(--green)"/><path d="M2.5 5 H7 M5 3 L7 5 L5 7" stroke="#fff" stroke-width="1.3" fill="none"/></svg>Major problems at the Department of Revenue</li>
    <li><svg width="10" height="10" viewBox="0 0 10 10"><circle cx="5" cy="5" r="5" fill="var(--green)"/><path d="M2.5 5 H7 M5 3 L7 5 L5 7" stroke="#fff" stroke-width="1.3" fill="none"/></svg>Indifference by the governor, current and past</li>
    <li><svg width="10" height="10" viewBox="0 0 10 10"><circle cx="5" cy="5" r="5" fill="var(--green)"/><path d="M2.5 5 H7 M5 3 L7 5 L5 7" stroke="#fff" stroke-width="1.3" fill="none"/></svg>Bad legislation</li>
    <li><svg width="10" height="10" viewBox="0 0 10 10"><circle cx="5" cy="5" r="5" fill="var(--green)"/><path d="M2.5 5 H7 M5 3 L7 5 L5 7" stroke="#fff" stroke-width="1.3" fill="none"/></svg>Bad case law</li>
    <li><svg width="10" height="10" viewBox="0 0 10 10"><circle cx="5" cy="5" r="5" fill="var(--green)"/><path d="M2.5 5 H7 M5 3 L7 5 L5 7" stroke="#fff" stroke-width="1.3" fill="none"/></svg>Major funding limitations</li>
    <li><svg width="10" height="10" viewBox="0 0 10 10"><circle cx="5" cy="5" r="5" fill="var(--green)"/><path d="M2.5 5 H7 M5 3 L7 5 L5 7" stroke="#fff" stroke-width="1.3" fill="none"/></svg>Little or no enforcement of uniformity</li>
  </ul>
  <ul class="col-b">
    <li><svg width="10" height="10" viewBox="0 0 10 10"><circle cx="5" cy="5" r="5" fill="var(--green)"/><path d="M2.5 5 H7 M5 3 L7 5 L5 7" stroke="#fff" stroke-width="1.3" fill="none"/></svg>Sale chasing</li>
    <li><svg width="10" height="10" viewBox="0 0 10 10"><circle cx="5" cy="5" r="5" fill="var(--green)"/><path d="M2.5 5 H7 M5 3 L7 5 L5 7" stroke="#fff" stroke-width="1.3" fill="none"/></svg>Fraudulent assessment work</li>
    <li><svg width="10" height="10" viewBox="0 0 10 10"><circle cx="5" cy="5" r="5" fill="var(--green)"/><path d="M2.5 5 H7 M5 3 L7 5 L5 7" stroke="#fff" stroke-width="1.3" fill="none"/></svg>Political interference in the valuation process</li>
    <li><svg width="10" height="10" viewBox="0 0 10 10"><circle cx="5" cy="5" r="5" fill="var(--green)"/><path d="M2.5 5 H7 M5 3 L7 5 L5 7" stroke="#fff" stroke-width="1.3" fill="none"/></svg>Lakeshore Realtors Guild’s</li>
    <li><svg width="10" height="10" viewBox="0 0 10 10"><circle cx="5" cy="5" r="5" fill="var(--green)"/><path d="M2.5 5 H7 M5 3 L7 5 L5 7" stroke="#fff" stroke-width="1.3" fill="none"/></svg>Limitations in the computer software to do mass appraisal</li>
  </ul>
</section>

<footer class="site-footer">
  <svg class="footer-band" width="950" height="220" viewBox="0 0 950 220">
    <path d="M0 130 Q475 -110 950 130 V220 H0 Z" fill="var(--green)"/>
    <path d="M0 143 Q475 -90 950 143 V220 H0 Z" fill="var(--ink)"/>
  </svg>
  <div class="footer-brand"><span class="brand-dot"></span>NPRB</div>
  <div class="footer-rule"></div>
  <div class="copyright">© 2022 NPRB &nbsp;|&nbsp; All Rights Reserved</div>
  <div class="legal"><a href="#">Privacy Policy</a><span>|</span><a href="#">Terms &amp; Conditions</a></div>
</footer>

</body>
</html>
```